Quarry Vale Business Cards

We need to design some upbeat business cards. We are an Industrial Rope Access Company/Height Safety Company that specialize in Rope Access, Confined Space, Anchor Points, Safety Systems, PPE Inspecions and Rigging.
Company name is Quarry Vale Ltd
Card is for Reggie Stanton the Company Director
His mobile number is 027 816 4920 and email is reggie@quarryvale.co.nz. Website address is www.quarryvale.co.nz.
We will post some pictures below to ensure you get a good idea of what we do.

```html
<!DOCTYPE html>
<html lang="en">
<head>
<meta charset="utf-8">
<title>Quarry Vale Ltd – Business Card</title>
<link href="https://fonts.googleapis.com/css2?family=Oswald:wght@500;600&family=Abel&family=Lora:wght@700&display=swap" rel="stylesheet">
<style>
  :root {
    --navy-deep: #21225a;
    --navy-mid: #333466;
    --band-cream: #e4e2d8;
    --band-ink: #3a3b6b;
    --text-cream: #ecebe0;
    --stage-dark: #8a8a8c;
    --stage-light: #ffffff;
  }
  * { margin: 0; padding: 0; box-sizing: border-box; }
  html, body { width: 1200px; height: 1000px; overflow: hidden; }
  body {
    position: relative;
    background: linear-gradient(180deg, var(--stage-dark) 0%, #cfcfd0 30%, var(--stage-light) 52%, #d4d4d5 75%, var(--stage-dark) 100%);
  }
  .card {
    position: absolute;
    left: 180px;
    width: 840px;
    height: 400px;
    overflow: hidden;
    color: var(--text-cream);
  }
  .card--front {
    top: 100px;
    background: linear-gradient(180deg, var(--navy-deep) 0%, var(--navy-mid) 50%, var(--navy-deep) 100%);
  }
  .brand-band {
    position: absolute;
    left: 63px;
    top: 0;
    width: 139px;
    height: 400px;
    background: var(--band-cream);
    display: flex;
    align-items: center;
    justify-content: center;
  }
  .brand-band__name {
    writing-mode: vertical-rl;
    transform: rotate(180deg);
    font-family: "Oswald", sans-serif;
    font-weight: 600;
    font-size: 42px;
    letter-spacing: 0.5px;
    color: var(--band-ink);
    white-space: nowrap;
  }
  .person {
    position: absolute;
    left: 444px;
    top: 40px;
  }
  .person__name {
    font-family: "Oswald", sans-serif;
    font-weight: 600;
    font-size: 44px;
    line-height: 1;
    letter-spacing: 0.5px;
  }
  .person__role {
    margin-top: 18px;
    font-family: "Abel", sans-serif;
    font-size: 27px;
    letter-spacing: 0.5px;
  }
  .divider {
    position: absolute;
    left: 444px;
    top: 179px;
    width: 306px;
    height: 3px;
    background: var(--text-cream);
  }
  .contacts {
    position: absolute;
    left: 458px;
    top: 250px;
    list-style: none;
  }
  .contacts__item {
    display: flex;
    align-items: center;
    height: 37px;
    font-family: "Lora", serif;
    font-weight: 700;
    font-size: 20px;
  }
  .contacts__icon {
    width: 38px;
    height: 24px;
    margin-right: 18px;
    flex: none;
  }
  .card--back {
    top: 542px;
    background: linear-gradient(180deg, var(--navy-deep) 0%, var(--navy-mid) 55%, var(--navy-deep) 100%);
  }
  .back-visual {
    position: absolute;
    inset: 0;
    background: radial-gradient(ellipse at 55% 40%, rgba(90, 92, 140, 0.35) 0%, rgba(33, 34, 90, 0) 70%);
  }
  .back-name {
    position: absolute;
    left: 0;
    right: 0;
    top: 170px;
    text-align: center;
    font-family: "Lora", serif;
    font-weight: 700;
    font-size: 44px;
    letter-spacing: 1px;
    color: var(--text-cream);
  }
</style>
</head>
<body>
  <section class="card card--front">
    <div class="brand-band">
      <span class="brand-band__name">QUARRY VALE LTD</span>
    </div>
    <div class="person">
      <h1 class="person__name">REGGIE STANTON</h1>
      <p class="person__role">Company Director</p>
    </div>
    <div class="divider"></div>
    <ul class="contacts">
      <li class="contacts__item">
        <svg class="contacts__icon" viewBox="0 0 38 24" aria-hidden="true">
          <path d="M2 9 Q19 -1 36 9 L33 12 L27 10 L27 7 Q19 4 11 7 L11 10 L5 12 Z" fill="var(--text-cream)"/>
          <path d="M10 11 L28 11 L33 22 L5 22 Z" fill="var(--text-cream)"/>
          <circle cx="19" cy="16" r="3.2" fill="var(--navy-mid)"/>
        </svg>
        027 816 4920
      </li>
      <li class="contacts__item">
        <svg class="contacts__icon" viewBox="0 0 38 24" aria-hidden="true">
          <rect x="3" y="4" width="32" height="17" fill="none" stroke="var(--text-cream)" stroke-width="2"/>
          <path d="M3 4 L19 15 L35 4" fill="none" stroke="var(--text-cream)" stroke-width="2"/>
        </svg>
        reggie@quarryvale.co.nz
      </li>
      <li class="contacts__item">
        <svg class="contacts__icon" viewBox="0 0 38 24" aria-hidden="true">
          <g fill="none" stroke="var(--text-cream)" stroke-width="1.5">
            <circle cx="20" cy="12" r="10"/>
            <ellipse cx="20" cy="12" rx="4.5" ry="10"/>
            <line x1="10" y1="12" x2="30" y2="12"/>
            <path d="M12 6.5 H28 M12 17.5 H28"/>
          </g>
        </svg>
        www.quarryvale.co.nz
      </li>
    </ul>
  </section>

  <section class="card card--back">
    <div class="back-visual" role="img" aria-label="Faint photograph of rope access work on a tall structure"></div>
    <h2 class="back-name">QUARRY VALE LTD</h2>
  </section>
</body>
</html>
```